Business Card for Graphic Design Firm

This project is for a new graphic design firm based in New Jersey called Velmoric. We outsource graphic design and marketing jobs. We want to communicate that this is a professional company but it as well creative and artistic. This card may be used as a horizontal double sided paper card or a vertical single sided translucent card so feel free to submit designs in whichever format or both.
Updates

Reason: Extending the deadline because I'm not exactly satisfied with the designs so far.

Please view the updated project brief

Target Market(s)

Adults aged 25-60

Industry/Entity Type

Graphic Design

Font styles to use
Serif
Sans Serif

Requirements
Nice to have
• Maybe a triangular pattern around the edges similar to our logo

```html
<!DOCTYPE html>
<html lang="en">
<head>
<meta charset="utf-8">
<title>Velmoric business card</title>
<link rel="stylesheet" href="https://fonts.googleapis.com/css2?family=Open+Sans:wght@400;600;700&display=swap">
<style>
  :root {
    --backdrop: #262627;
    --card: #c6c8ca;
    --card-edge: #d6d8da;
    --orange: #f08a1c;
    --teal: #1a9bb0;
    --ink-grey: #8d9093;
    --mark-grey: #a9acaf;
  }
  * { margin: 0; padding: 0; box-sizing: border-box; }
  html, body {
    width: 1200px;
    height: 1000px;
    overflow: hidden;
    background: var(--backdrop);
    font-family: "Open Sans", sans-serif;
  }
  .card {
    position: absolute;
    left: 110px;
    top: 210px;
    width: 980px;
    height: 580px;
    border-radius: 34px;
    background: linear-gradient(160deg, var(--card-edge) 0%, var(--card) 55%, #bfc1c3 100%);
  }
  .holder {
    position: absolute;
    right: 70px;
    top: 70px;
    text-align: right;
  }
  .holder-name {
    color: var(--orange);
    font-weight: 700;
    font-size: 34px;
    letter-spacing: 1px;
    line-height: 1.1;
  }
  .holder-position {
    color: var(--orange);
    font-size: 30px;
    line-height: 1.1;
  }
  .unit {
    position: absolute;
    right: 70px;
    top: 200px;
    text-align: right;
  }
  .unit-company {
    color: var(--teal);
    font-weight: 700;
    font-size: 34px;
    letter-spacing: 1px;
    line-height: 1.1;
  }
  .unit-department {
    color: var(--teal);
    font-size: 30px;
    line-height: 1.1;
  }
  .contact {
    position: absolute;
    right: 70px;
    top: 320px;
    text-align: right;
    list-style: none;
    color: var(--ink-grey);
    font-size: 25px;
    line-height: 1.36;
  }
  .brand {
    position: absolute;
    left: 60px;
    bottom: 70px;
    display: flex;
    align-items: center;
    gap: 22px;
  }
  .brand-square {
    width: 46px;
    height: 46px;
    background: var(--mark-grey);
  }
  .brand-name {
    color: var(--mark-grey);
    font-weight: 400;
    font-size: 72px;
    letter-spacing: 6px;
    line-height: 1;
    text-transform: uppercase;
  }
</style>
</head>
<body>
  <article class="card">
    <div class="brand">
      <span class="brand-square"></span>
      <span class="brand-name">Velmoric</span>
    </div>

    <header class="holder">
      <p class="holder-name">NAME SURNAME</p>
      <p class="holder-position">position</p>
    </header>

    <section class="unit">
      <p class="unit-company">VELMORIC</p>
      <p class="unit-department">department</p>
    </section>

    <ul class="contact">
      <li>New Jersey,</li>
      <li>Linden str. 42</li>
      <li>Tel: +12015550148</li>
      <li>Mob: +12015550148</li>
      <li>namesurname@velmoric.net</li>
      <li>www.velmoric.net</li>
    </ul>
  </article>
</body>
</html>
```